We Kill Spreadsheets - Sticker Design

At Vantrel, we're a custom software development company. We build apps, websites, and databases to help teams innovate and manage their data. ...and we kill spreadsheets. Many professional people know what we're talking about: emailing docs back-and-forth, rooting around for the latest version, drowning in some massive thousand-column scrolling nightmare, trying to find that tiny mistake in a formula somewhere, accidentally deleting a cell... it goes on and on. We save teams from spreadsheet hell. We build shared solutions, relational data systems, workflow apps, amazing reporting tools, dashboards, and more.<br/><br/>We're looking for a fun, whimsical, sticker using some of our brand elements, but that communicates the idea without being too corporate. We don't need our logo on the sticker... but we want people who know our brand to recognize the colors, or shapes, or styles. (Sort of like how Fizzabo Pop does red-themed campaigns with polar bears and we all know it's their brand.) We also don't want to get sued by Quandrix, so don't use anything with a trademarked Tably image.<br/><br/>We want this to spark conversation. The image can be funny, irreverent, artistic, clever, provocative. It can be whatever size or shape you wish.<br/><br/>Use these guidelines! https://www.decalharbor.example/artwork<br/><br/>Also attached are our brand materials. Please use them!

Target Market(s)

Tech-savvy professionals.

Industry/Entity Type

Software Development

Font styles to use
Sans Serif

Colors

Designer to choose colors to be used in the design.

Requirements
Must have
• The sticker should say, "We Kill Spreadsheets".
• Vantrel colors and style -- when you see this, it should seem like it fits with our brand.
• Colors -- please see attached brand materials!
• Fonts -- please see attached brand materials!
Nice to have
• We want the sticker to be smart, funny, clever... the idea is to spark conversation. Don't just make a spreadsheet icon with a target on it... that's too literal and doesn't really seem creative.
Should not have
• No Tably or other actual brand elements from spreadsheet companies!

```html
<!DOCTYPE html>
<html lang="en">
<head>
<meta charset="utf-8">
<title>We Kill Spreadsheets – Sticker</title>
<link href="https://fonts.googleapis.com/css2?family=Montserrat:wght@500;900&display=swap" rel="stylesheet">
<style>
  :root {
    --page-bg: #ffffff;
    --cut-line: #d9408e;
    --band-green: #36a97a;
    --band-teal: #20ad9f;
    --band-blue: #2f8acb;
    --band-indigo: #4a5fb0;
    --band-violet: #5b5aa8;
    --ink-dark: #1b232c;
    --ink-light: #ffffff;
  }
  html, body {
    margin: 0;
    padding: 0;
    width: 1040px;
    height: 1200px;
    overflow: hidden;
    background: var(--page-bg);
  }
  .canvas {
    position: relative;
    width: 1040px;
    height: 1200px;
  }
  .sticker {
    position: absolute;
    left: 0;
    top: 362px;
    width: 1040px;
    height: 476px;
  }
  .cut-line { fill: var(--page-bg); stroke: var(--cut-line); stroke-width: 2; }
  .headline {
    font-family: "Montserrat", sans-serif;
    font-weight: 900;
    fill: var(--ink-light);
  }
  .subline {
    font-family: "Montserrat", sans-serif;
    font-weight: 900;
    fill: var(--ink-dark);
  }
  .brand-name {
    font-family: "Montserrat", sans-serif;
    font-weight: 500;
    fill: var(--ink-light);
  }
  .brand-dot { fill: var(--ink-light); }
</style>
</head>
<body>
<div class="canvas">
  <svg class="sticker" viewBox="0 90 1792 820" xmlns="http://www.w3.org/2000/svg">
    <defs>
      <linearGradient id="band-gradient" x1="185" y1="0" x2="1556" y2="0" gradientUnits="userSpaceOnUse">
        <stop offset="0" stop-color="var(--band-green)"/>
        <stop offset="0.35" stop-color="var(--band-teal)"/>
        <stop offset="0.62" stop-color="var(--band-blue)"/>
        <stop offset="0.82" stop-color="var(--band-indigo)"/>
        <stop offset="1" stop-color="var(--band-violet)"/>
      </linearGradient>
    </defs>

    <rect class="cut-line" x="108" y="112" width="1572" height="600" rx="90"/>

    <rect class="band-artwork" x="185" y="212" width="1371" height="318" fill="url(#band-gradient)"
          role="img" aria-label="Green to violet torn paper band artwork taped over a faint spreadsheet grid"/>

    <g class="brand">
      <circle class="brand-dot" cx="380" cy="244" r="15"/>
      <text class="brand-name" x="406" y="254" font-size="30" letter-spacing="1">Vantrel</text>
    </g>

    <text class="headline" x="325" y="452" font-size="222" textLength="1165" lengthAdjust="spacingAndGlyphs">WE KILL</text>
    <text class="subline" x="340" y="640" font-size="112" textLength="1145" lengthAdjust="spacingAndGlyphs">SPREADSHEETS</text>
  </svg>
</div>
</body>
</html>
```